Jest Harbor Website - Corporate Comedy Show

I've created a company called "Jest Harbor". We put on corporate comedy shows for companies all over the country. I'd like to design a nice, sleek, professional website, similar to Ridora's: https://www.ridora-example.com. We like the one page layout.
Tagline: Your Team's Desk-Grin Ratio
I need the following sections:
1. first section would be scrolling images of the company logo and tagline, with 2 or 3 other scrolling images. Testimonials.
2. The next section below would be an about the company section. a small paragraph describing what we do.
4. The next section below would be for a promo video
5. The next section below would be for bios...my partner and I would have transparent head shots, side by side split-screen. When you hover over our headshots, a button for "bio" appears. When you click the "bio" button, an expanded bio appears.
6. Contact section. Newsletter subscription. A section where people enter their email and short message of what they're linking for that will link directly to our email addresses.
7. Additional content. Scrolling video gallery of our sketch videos. (a section that links to a page with videos and content)
Target Market(s)
Corporate Executives, Event Planners, Event Coordinators, Marketing and HR managers, Venue owners
Industry/Entity Type
It Company
Coding
Coded - Design and coding required
Number of Pages Required
1 page
Font styles to use
Other font styles liked:
- FunctionPro
Requirements
Must have
- -Please use the branded colors from the logo. Burgundy and Blue;
- -A contact section where people put in their email address, company they are from and a small memo to describe the event they're hosting, which will then get sent directly to our email accounts;
- -email accounts that are "marcus@thejestharbor-example.com" and "oliver@thejestharbor-example.com" that link to our zipmail accounts
- -getting our domain linked and hosted and all setup (www.thejestharbor-example.com- bought from SiteBarn)
Nice to have
- Build in Plotly Pages because we are familiar with it and know how to update
Should not have
- basic, generic look. too much white space (but soon is good!)

```html
<!DOCTYPE html>
<html lang="en">
<head>
<meta charset="utf-8">
<title>Jest Harbor — Video Gallery &amp; Contact</title>
<link href="https://fonts.googleapis.com/css2?family=Jost:wght@400;500&family=Open+Sans:wght@400;600&family=Roboto:wght@400;500&display=swap" rel="stylesheet">
<style>
  :root {
    --burgundy: #8a0a1f;
    --ink: #2a2a2a;
    --band: #363636;
    --muted: #7d7d7d;
    --white: #ffffff;
    --rule: #3a3a3a;
    --map-light: #e6e6e6;
    --map-mid: #cfcfcf;
    --map-dark: #a9a9a9;
  }
  * { box-sizing: border-box; margin: 0; padding: 0; }
  html, body { width: 1200px; height: 1000px; overflow: hidden; background: var(--white); }
  body { position: relative; font-family: "Open Sans", sans-serif; }

  .section-title {
    position: absolute; left: 0; text-align: center;
    font-family: "Jost", sans-serif; font-weight: 400; font-size: 27px;
    letter-spacing: 0.6px; color: var(--ink);
  }
  .section-intro {
    position: absolute; left: 252px; width: 630px; text-align: center;
    font-size: 14.5px; line-height: 19px; color: var(--muted);
  }

  .gallery-title { top: 15px; width: 1162px; }
  .gallery-intro { top: 94px; }
  .carousel { position: absolute; left: 0; top: 160px; }

  .gallery-caption {
    position: absolute; left: 421px; top: 420px; width: 302px; height: 56px;
    background: var(--burgundy); color: var(--white);
    display: flex; align-items: center; justify-content: center;
    font-size: 14.5px;
  }

  .gallery-track { position: absolute; left: 118px; top: 513px; width: 908px; height: 1px; background: var(--rule); }
  .gallery-progress { position: absolute; left: 397px; top: 512px; width: 117px; height: 3px; background: var(--burgundy); }

  .gallery-control { position: absolute; top: 547px; height: 33px; }
  .btn-all {
    left: 865px; width: 77px; background: var(--burgundy); color: var(--white);
    display: flex; align-items: center; justify-content: center; gap: 6px;
    font-family: "Roboto", sans-serif; font-size: 11px; font-weight: 400;
  }
  .btn-prev { left: 951px; width: 33px; background: var(--ink); }
  .btn-next { left: 992px; width: 33px; background: var(--burgundy); }
  .gallery-control svg { display: block; }
  .btn-prev svg, .btn-next svg { margin: 10px auto; }

  .social-band { position: absolute; left: 0; top: 630px; width: 1200px; height: 61px; background: var(--band); }
  .band-label {
    position: absolute; top: 18px; font-family: "Jost", sans-serif;
    font-size: 16px; color: var(--white); letter-spacing: 0.3px;
  }
  .follow-label { left: 122px; }
  .newsletter-label { left: 510px; }
  .social-link {
    position: absolute; top: 13px; width: 40px; height: 34px;
    display: flex; align-items: center; justify-content: center;
    font-family: "Open Sans", sans-serif; font-size: 10px; font-weight: 600; color: var(--white);
  }
  .social-link.is-active::before {
    content: ""; position: absolute; left: 3px; top: 0; width: 34px; height: 34px;
    border-radius: 50%; background: var(--burgundy); z-index: -1;
  }
  .social-link.is-active { z-index: 1; }
  .newsletter-input {
    position: absolute; left: 633px; top: 14px; width: 334px; height: 32px;
    background: var(--white); font-family: "Roboto", sans-serif;
    font-size: 10px; color: #555; padding: 10px 15px;
  }
  .newsletter-submit {
    position: absolute; left: 967px; top: 14px; width: 62px; height: 32px;
    background: var(--burgundy); color: var(--white);
    font-family: "Roboto", sans-serif; font-size: 11px; font-weight: 500;
    display: flex; align-items: center; justify-content: center;
  }

  .contact-title { top: 739px; width: 1136px; }
  .contact-intro { top: 818px; }

  .contact-map {
    position: absolute; left: 0; top: 919px; width: 1200px; height: 81px;
    background:
      linear-gradient(180deg, rgba(255,255,255,0.25), rgba(0,0,0,0.06)),
      linear-gradient(90deg, var(--map-dark) 0%, var(--map-mid) 8%, var(--map-light) 40%, var(--map-mid) 55%, var(--map-light) 75%, var(--map-mid) 100%);
  }
  .contact-panel { position: absolute; left: 123px; top: 919px; width: 287px; height: 81px; background: var(--burgundy); }
</style>
</head>
<body>

<h2 class="section-title gallery-title">VIDEO GALLERY</h2>
<p class="section-intro gallery-intro">Mauris a massa id leo aliquam consequat porttitor vitae est. Proin ultricies velit sed porttitor viverra. Pellen-tesque eget tristique est.</p>

<svg class="carousel" width="1200" height="320" viewBox="0 160 1200 320">
  <defs>
    <linearGradient id="still-orange" x1="0" y1="0" x2="1" y2="1">
      <stop offset="0" stop-color="#e0472a"/><stop offset="0.55" stop-color="#b23a26"/><stop offset="1" stop-color="#3a2a26"/>
    </linearGradient>
    <linearGradient id="still-grey" x1="0" y1="0" x2="0" y2="1">
      <stop offset="0" stop-color="#d8d8d6"/><stop offset="0.45" stop-color="#9a9894"/><stop offset="1" stop-color="#24201f"/>
    </linearGradient>
    <linearGradient id="still-main" x1="0" y1="0" x2="0" y2="1">
      <stop offset="0" stop-color="#2a1512"/><stop offset="0.25" stop-color="#7a2a20"/><stop offset="0.55" stop-color="#9a4a30"/><stop offset="0.8" stop-color="#3a2019"/><stop offset="1" stop-color="#150e0d"/>
    </linearGradient>
    <linearGradient id="still-main-side" x1="0" y1="0" x2="1" y2="0">
      <stop offset="0" stop-color="#a01818" stop-opacity="0.45"/><stop offset="0.4" stop-color="#a01818" stop-opacity="0"/><stop offset="0.7" stop-color="#000" stop-opacity="0"/><stop offset="1" stop-color="#000" stop-opacity="0.3"/>
    </linearGradient>
    <linearGradient id="still-rose" x1="0" y1="0" x2="1" y2="1">
      <stop offset="0" stop-color="#c7705e"/><stop offset="0.5" stop-color="#6a3a40"/><stop offset="1" stop-color="#221a22"/>
    </linearGradient>
    <linearGradient id="still-brick" x1="0" y1="0" x2="1" y2="0">
      <stop offset="0" stop-color="#2a1818"/><stop offset="0.15" stop-color="#a3141a"/><stop offset="0.35" stop-color="#5a2020"/><stop offset="0.65" stop-color="#6e5a4e"/><stop offset="1" stop-color="#3a302c"/>
    </linearGradient>
    <linearGradient id="still-floor" x1="0" y1="0" x2="0" y2="1">
      <stop offset="0.6" stop-color="#000" stop-opacity="0"/><stop offset="1" stop-color="#000" stop-opacity="0.55"/>
    </linearGradient>
  </defs>
  <g role="img" aria-label="Video still: two comedians on an orange club stage">
    <polygon points="118,235 295,252 295,418 120,435" fill="url(#still-orange)"/>
  </g>
  <g role="img" aria-label="Video still: comedian with microphone facing an audience">
    <polygon points="303,234 420,250 420,420 303,440" fill="url(#still-grey)"/>
  </g>
  <g role="img" aria-label="Video still: comedian performing to a crowd in a warm-lit room">
    <polygon points="723,250 840,234 841,440 723,420" fill="url(#still-rose)"/>
  </g>
  <g role="img" aria-label="Video still: comedian on a stage with red curtains and a brick wall">
    <polygon points="849,252 1026,235 1026,435 849,418" fill="url(#still-brick)"/>
    <polygon points="849,252 1026,235 1026,435 849,418" fill="url(#still-floor)"/>
  </g>
  <g role="img" aria-label="Featured video: corporate comedy show in a club with red curtains">
    <rect x="421" y="173" width="302" height="247" fill="url(#still-main)"/>
    <rect x="421" y="173" width="302" height="247" fill="url(#still-main-side)"/>
  </g>
  <circle cx="572" cy="323" r="20" fill="none" stroke="#fff" stroke-width="2.5"/>
  <polygon points="566,312 566,334 582,323" fill="#fff"/>
</svg>

<div class="gallery-caption">Corporate Comedy Shows</div>
<div class="gallery-track"></div>
<div class="gallery-progress"></div>

<a class="gallery-control btn-all">
  <svg width="14" height="8" viewBox="0 0 14 8"><path d="M0 4H13M9.5 0.5L13 4L9.5 7.5" stroke="#fff" stroke-width="1.3" fill="none"/></svg>ALL
</a>
<a class="gallery-control btn-prev" aria-label="Previous">
  <svg width="8" height="13" viewBox="0 0 8 13"><path d="M7 1L1.5 6.5L7 12" stroke="#fff" stroke-width="1.6" fill="none"/></svg>
</a>
<a class="gallery-control btn-next" aria-label="Next">
  <svg width="8" height="13" viewBox="0 0 8 13"><path d="M1 1L6.5 6.5L1 12" stroke="#fff" stroke-width="1.6" fill="none"/></svg>
</a>

<section class="social-band">
  <span class="band-label follow-label">FOLLOW US</span>
  <a class="social-link" style="left:230px">Chirp</a>
  <a class="social-link" style="left:277px">Facet</a>
  <a class="social-link is-active" style="left:325px">Pinrow</a>
  <a class="social-link" style="left:372px">Drablo</a>
  <span class="band-label newsletter-label">NEWSLETTER</span>
  <div class="newsletter-input">Enter your email...</div>
  <div class="newsletter-submit">SUBMIT</div>
</section>

<h2 class="section-title contact-title">CONTACT US</h2>
<p class="section-intro contact-intro">Mauris a massa id leo aliquam consequat porttitor vitae est. Proin ultricies velit sed porttitor viverra. Pellen-tesque eget tristique est.</p>

<div class="contact-map" role="img" aria-label="Greyscale street map showing the venue location"></div>
<div class="contact-panel"></div>

</body>
</html>
```